New Digital Marketing Company Needs Web Design

Introduction

Brightcrest gives advice to small businesses about their websites and digital marketing strategies and builds working relationships with clients to understand their business and maximise its online presence.

Brightcrest offers services to support its clients needs such as: website auditing & search engine optimisation (SEO), Quorvo Promoline, Chatterlane advertising, newsletter development & management, online performance reporting, email setup & management, website hosting, maintenance & backup, web development, web updates & web design.

Design Specification

The site should have a clean & professional look and use the colour scheme from the logo (attached below).

The design should consist of 2 templates; The homepage & content page.

Homepage Design

The homepage should have a header with logo, contact number and email and menu. Followed underneath by a slider and then individual blocks for key services. Under the key services should be a testimonial block with 3 testimonials. Finally the footer with company details, menu links and location map.

Header Info:

Contact number: 01632 960481
Email: info@brightcrest-demo.co.uk

Menu: Home Services About Contact

Slider Design:

The slider should be full page and show an image with text.

Key Services:

The key services should have a relevant icon and brief description.

The key services are:

Digital Marketing

Website Hosting & Management

Website Health Check (SEO)

Website Updating & Development

Newsletter Management

Email Management

Note: Lorem Ipsum can be used for brief description...

Testimonials:

There should be 3 testimonials side by side and they should include a headshot image of the person giving the testimonial.

Note: Lorem Ipsum and sample images can be used for testimonials...

Footer:

The footer should have 3 sections:

Menu links:

Digital Marketing About
Quorvo Promoline Contact
Chatterlane Advertising Privacy Policy
Search Engine Optimisation (SEO) Terms & Conditions
Website Hosting FAQ
Newsletter Management

Company Information:

BrightCrest
14 Marlow Close
Fernhollow
Ashdale
ZZ9 4QT
Tel: 01632 960481

Chatterlane icon - Pipwave icon - Careernest icon

Location

Quorvo map

Footer Bottom:

Copyright message.

Content Design

The content design should have the common header and footer.

Each content page should have a banner for image with text description (page title).

The content page should have area for text description and area for a video display if available.

There should be a right column (possibly) for modules (latest blog, latest Chatterlane feeds, testimonial)

Project Deadline Extended
Reason: I have had to extend the deadline as could not review while on vacation and need to feedback to some designers for content page design. Many thanks for your understanding.

Target Market(s)

Industry/Entity Type

Digital

Number of Pages Required

2 page

Requirements
Must have
• The site should have a clean & professional look and use the colour scheme from the logo (attached below).
• The design should consist of 2 templates; The homepage & content page.

```html
<!DOCTYPE html>
<html lang="en">
<head>
<meta charset="utf-8">
<title>BrightCrest – Digital Marketing</title>
<link rel="stylesheet" href="https://fonts.googleapis.com/css2?family=Ubuntu:wght@400;500;700&family=Lato:wght@400;700&display=swap">
<style>
:root{
  --plum:#6b1848;
  --ink:#3d3150;
  --topbar:#463a5b;
  --text:#333;
  --muted:#666;
  --line:#dcdcdc;
  --bulb:#e4e4e6;
  --footer:#1f1f1f;
  --footer-base:#121212;
  --footer-text:#b5b5b5;
  --white:#fff;
}
*{box-sizing:border-box;margin:0;padding:0}
html,body{width:1200px;height:2190px;overflow:hidden}
body{position:relative;font-family:'Lato',Arial,sans-serif;color:var(--text);background:var(--white)}
.abs{position:absolute}
/* top bar */
.topbar{left:0;top:0;width:1200px;height:30px;background:var(--topbar);color:var(--white);font-size:12.5px}
.topbar .call{left:100px;top:8px}
.topbar .mail{left:754px;top:8px}
.topbar .social{left:982px;top:0;display:flex}
.topbar .social span{width:29px;height:30px;border-left:1px solid rgba(255,255,255,.18);display:flex;align-items:center;justify-content:center}
.topbar .social span.on{background:var(--plum)}
.topbar .social i{width:9px;height:9px;background:var(--white);display:block}
/* header */
.header{left:0;top:30px;width:1200px;height:74px;background:var(--white);border-bottom:1px solid #eee}
.brand{left:98px;top:20px;display:flex;align-items:center;gap:8px}
.brand-mark{width:30px;height:30px;border-radius:50%;background:var(--ink)}
.brand-name{font-family:'Ubuntu',sans-serif;font-weight:700;font-size:30px;color:var(--ink);line-height:1}
.nav{left:686px;top:0;display:flex;height:74px}
.nav a{display:flex;align-items:center;padding:0 28px;font-size:15px;color:#444;text-decoration:none}
.nav a.active{background:#f3f3f3;color:var(--plum);font-weight:700;border-bottom:3px solid var(--plum);padding:0 23px}
/* hero */
.hero{left:0;top:104px;width:1200px;height:471px;background:linear-gradient(180deg,#4e5e6a,#475763)}
.hero-title{left:0;top:188px;width:1200px;text-align:center;font-family:'Ubuntu',sans-serif;font-weight:700;font-size:36px;color:var(--white);letter-spacing:.5px}
.hero-text{left:220px;top:236px;width:760px;text-align:center;font-size:15.5px;line-height:22px;color:var(--white)}
.btn{display:flex;align-items:center;justify-content:center;font-size:13px;letter-spacing:.4px;text-decoration:none}
.btn-primary{left:446px;top:304px;width:146px;height:42px;background:var(--plum);color:var(--white)}
.btn-light{left:609px;top:304px;width:145px;height:42px;background:var(--white);color:#222}
.dots{left:572px;top:530px;display:flex;gap:8px;align-items:center}
.dots i{width:11px;height:11px;border-radius:50%;border:2px solid var(--white);background:transparent}
.dots i.on{width:15px;height:15px;background:var(--plum)}
/* section heads */
.sec-title{left:0;width:1200px;text-align:center;font-family:'Ubuntu',sans-serif;font-weight:500;font-size:32px;color:#2b2b2b}
.sec-title b{color:var(--plum);font-weight:500}
.sec-bulb{left:588px}
.lead{left:220px;top:727px;width:760px;text-align:center;font-size:12.5px;line-height:19px;color:#333}
/* services */
.service{width:263px;text-align:center}
.service svg{display:block;margin:0 auto}
.service h3{font-family:'Ubuntu',sans-serif;font-weight:400;font-size:17.5px;line-height:24px;color:#222;margin-top:8px;height:48px;display:flex;align-items:center;justify-content:center}
.service p{font-size:12.5px;line-height:20px;color:var(--muted);margin-top:6px}
.service .go{width:20px;height:20px;border-radius:50%;background:#333;margin:16px auto 0;display:flex;align-items:center;justify-content:center}
.vline{width:1px;background:var(--line)}
.hline{height:1px;background:var(--line)}
/* testimonials */
.testimonials{left:0;top:1456px;width:1200px;height:420px;background:linear-gradient(180deg,#efefef,#e9e9e9)}
.card{top:1603px;width:317px;height:212px;background:var(--white);border:1px solid #e2e2e2;padding:26px 24px 0 26px}
.card p{font-size:12.5px;line-height:25px;color:#222}
.person{display:flex;align-items:center;gap:14px;margin-top:24px}
.avatar{width:76px;height:76px;border-radius:50%;border:3px solid var(--ink);background:linear-gradient(160deg,#c9b9ae,#7f746f)}
.person strong{display:block;font-family:'Ubuntu',sans-serif;font-weight:500;font-size:15.5px;color:var(--plum)}
.person span{font-size:12.5px;color:#333}
/* footer */
.footer{left:0;top:1876px;width:1200px;height:270px;background:var(--footer)}
.col{top:1920px;color:var(--footer-text)}
.col h4{font-family:'Ubuntu',sans-serif;font-weight:500;font-size:18.5px;color:var(--white)}
.quick ul{list-style:none;margin-top:12px}
.quick li{font-size:13px;line-height:31px;color:var(--footer-text)}
.quick li::before{content:"›";color:var(--white);margin-right:12px;font-size:15px}
.news p,.contact p{font-size:13px;line-height:23px;margin-top:12px;color:var(--footer-text)}
.field{margin-top:13px;width:210px;height:37px;background:#444;border:1px solid #555;color:var(--white);font-size:13px;padding:10px 12px}
.subscribe{margin-top:13px;width:128px;height:38px;background:var(--white);color:#222;font-size:15px;display:flex;align-items:center;justify-content:center}
.contact p{line-height:24.5px}
.soc{display:flex;gap:12px;margin-top:14px}
.soc i{width:24px;height:24px;background:#2a79b8;display:block}
.map{left:816px;top:1923px;width:283px;height:153px;background:linear-gradient(135deg,#b9cfa2 0%,#d6dcc9 45%,#9cc3d9 100%)}
.map-link{left:816px;top:2083px;font-size:12.5px;color:var(--footer-text);text-decoration:underline}
.base{left:0;top:2146px;width:1200px;height:44px;background:var(--footer-base);color:var(--white);font-size:13.5px;display:flex;align-items:center;justify-content:center}
</style>
</head>
<body>

<svg width="0" height="0" style="position:absolute" aria-hidden="true">
  <defs>
    <symbol id="bulb" viewBox="0 0 100 130">
      <circle cx="50" cy="40" r="33" fill="none" stroke="var(--bulb)" stroke-width="7"/>
      <path d="M38 71 L38 82 L62 82 L62 71" fill="none" stroke="var(--bulb)" stroke-width="7"/>
      <rect x="38" y="88" width="24" height="5" rx="2.5" fill="var(--bulb)"/>
      <rect x="40" y="97" width="20" height="5" rx="2.5" fill="var(--bulb)"/>
      <rect x="44" y="106" width="12" height="4" rx="2" fill="var(--bulb)"/>
      <ellipse cx="50" cy="124" rx="48" ry="4" fill="#ececec"/>
    </symbol>
    <symbol id="bulb-on" viewBox="0 0 100 130">
      <circle cx="50" cy="40" r="33" fill="none" stroke="var(--ink)" stroke-width="7"/>
      <path d="M38 71 L38 82 L62 82 L62 71" fill="none" stroke="var(--ink)" stroke-width="7"/>
      <rect x="38" y="88" width="24" height="5" rx="2.5" fill="var(--ink)"/>
      <rect x="40" y="97" width="20" height="5" rx="2.5" fill="var(--ink)"/>
      <rect x="44" y="106" width="12" height="4" rx="2" fill="var(--ink)"/>
      <ellipse cx="50" cy="124" rx="48" ry="4" fill="#ececec"/>
    </symbol>
    <symbol id="arrow" viewBox="0 0 10 10">
      <path d="M4 2 L7 5 L4 8" fill="none" stroke="#fff" stroke-width="1.6"/>
    </symbol>
  </defs>
</svg>

<!-- top bar -->
<div class="abs topbar">
  <div class="abs call">☏&nbsp; Call Us : 01632 960481</div>
  <div class="abs mail">✉&nbsp; Email: info@brightcrest-demo.co.uk</div>
  <div class="abs social">
    <span><i></i></span><span class="on"><i></i></span><span><i></i></span><span><i></i></span>
  </div>
</div>

<!-- header -->
<header class="abs header">
  <div class="abs brand"><span class="brand-mark"></span><span class="brand-name">BrightCrest</span></div>
  <nav class="abs nav">
    <a class="active" href="#">Home</a><a href="#">About Us</a><a href="#">Services</a><a href="#">Contact Us</a>
  </nav>
</header>

<!-- hero -->
<section class="abs hero" role="img" aria-label="Flat illustration of a desk seen from above with hands working on a laptop, charts, tablet and paperwork"></section>
<h1 class="abs hero-title">WELCOME TO BRIGHTCREST</h1>
<p class="abs hero-text">Brightcrest gives advice to small businesses about their websites and digital marketing strategies and builds working relationships with clients to understand their business and maximise its online presence.</p>
<a class="abs btn btn-primary" href="#">LEARN MORE</a>
<a class="abs btn btn-light" href="#">CONTACT NOW</a>
<div class="abs dots"><i></i><i class="on"></i><i></i></div>

<!-- services -->
<h2 class="abs sec-title" style="top:626px">Our <b>Services</b></h2>
<svg class="abs sec-bulb" style="top:678px" width="24" height="30" viewBox="0 0 100 130"><use href="#bulb"/></svg>
<p class="abs lead">Lorem Ipsum is simply dummy text of the printing and typesettingem Ipsum has been the industry's standard dummy text ever since the 1500s, when an unknown printer took a gallebled it to make a type specimen book.</p>

<div class="abs vline" style="left:324px;top:830px;height:242px"></div>
<div class="abs vline" style="left:588px;top:830px;height:242px"></div>
<div class="abs vline" style="left:853px;top:830px;height:242px"></div>
<div class="abs hline" style="left:92px;top:1104px;width:206px"></div>
<div class="abs hline" style="left:350px;top:1104px;width:206px"></div>
<div class="abs hline" style="left:614px;top:1104px;width:206px"></div>
<div class="abs hline" style="left:877px;top:1104px;width:206px"></div>
<div class="abs vline" style="left:324px;top:1138px;height:242px"></div>
<div class="abs vline" style="left:588px;top:1138px;height:242px"></div>
<div class="abs vline" style="left:853px;top:1138px;height:242px"></div>

<div class="abs service" style="left:64px;top:813px">
  <svg width="100" height="130" viewBox="0 0 100 130"><use href="#bulb"/><circle cx="46" cy="38" r="9" fill="none" stroke="var(--ink)" stroke-width="4"/><path d="M52 45 L60 53" stroke="var(--ink)" stroke-width="5"/></svg>
  <h3>Website Auditing<br>&amp; (SEO)</h3>
  <p>printing and typesetting istry.<br>Ipsum has been the industry's sta.</p>
  <div class="go"><svg width="10" height="10"><use href="#arrow"/></svg></div>
</div>
<div class="abs service" style="left:324px;top:813px">
  <svg width="100" height="130" viewBox="0 0 100 130"><use href="#bulb-on"/><rect x="38" y="36" width="5" height="12" fill="var(--ink)"/><rect x="47" y="30" width="5" height="18" fill="var(--ink)"/><rect x="56" y="33" width="5" height="15" fill="var(--ink)"/></svg>
  <h3>Quorvo<br>Promoline</h3>
  <p>printing and typesetting istry.<br>Ipsum has been the industry's sta.</p>
  <div class="go"><svg width="10" height="10"><use href="#arrow"/></svg></div>
</div>
<div class="abs service" style="left:588px;top:813px">
  <svg width="100" height="130" viewBox="0 0 100 130"><use href="#bulb"/><circle cx="44" cy="42" r="7" fill="none" stroke="var(--ink)" stroke-width="4"/><path d="M50 48 L64 30" stroke="var(--ink)" stroke-width="5"/></svg>
  <h3>Web<br>Development</h3>
  <p>printing and typesetting istry.<br>Ipsum has been the industry's sta.</p>
  <div class="go"><svg width="10" height="10"><use href="#arrow"/></svg></div>
</div>
<div class="abs service" style="left:852px;top:813px">
  <svg width="100" height="130" viewBox="0 0 100 130"><use href="#bulb"/><rect x="38" y="28" width="24" height="24" fill="none" stroke="var(--ink)" stroke-width="3.5"/><path d="M43 35 H57 M43 40 H57 M43 45 H57" stroke="var(--ink)" stroke-width="2.5"/></svg>
  <h3>Newsletter Development<br>&amp; Management</h3>
  <p>printing and typesetting istry.<br>Ipsum has been the industry's sta.</p>
  <div class="go"><svg width="10" height="10"><use href="#arrow"/></svg></div>
</div>

<div class="abs service" style="left:64px;top:1122px">
  <svg width="100" height="130" viewBox="0 0 100 130"><use href="#bulb"/><rect x="34" y="30" width="32" height="20" fill="none" stroke="var(--ink)" stroke-width="3.5"/><path d="M40 44 L46 38 L52 42 L60 34" fill="none" stroke="var(--plum)" stroke-width="3"/></svg>
  <h3>Online Performance<br>Reporting</h3>
  <p>printing and typesetting istry.<br>Ipsum has been the industry's sta.</p>
  <div class="go"><svg width="10" height="10"><use href="#arrow"/></svg></div>
</div>
<div class="abs service" style="left:324px;top:1122px">
  <svg width="100" height="130" viewBox="0 0 100 130"><use href="#bulb"/><rect x="35" y="34" width="30" height="20" fill="var(--ink)"/><path d="M35 34 L50 46 L65 34" fill="none" stroke="#fff" stroke-width="2.5"/><circle cx="50" cy="28" r="5" fill="var(--plum)"/></svg>
  <h3>Email Setup &amp;<br>Management</h3>
  <p>printing and typesetting istry.<br>Ipsum has been the industry's sta.</p>
  <div class="go"><svg width="10" height="10"><use href="#arrow"/></svg></div>
</div>
<div class="abs service" style="left:588px;top:1122px">
  <svg width="100" height="130" viewBox="0 0 100 130"><use href="#bulb"/><circle cx="50" cy="40" r="15" fill="none" stroke="var(--ink)" stroke-width="4"/><path d="M35 40 H65 M50 25 V55" stroke="var(--ink)" stroke-width="2.5"/></svg>
  <h3>Website<br>Hosting</h3>
  <p>printing and typesetting istry.<br>Ipsum has been the industry's sta.</p>
  <div class="go"><svg width="10" height="10"><use href="#arrow"/></svg></div>
</div>
<div class="abs service" style="left:852px;top:1122px">
  <svg width="100" height="130" viewBox="0 0 100 130"><use href="#bulb"/><ellipse cx="46" cy="31" rx="11" ry="4" fill="var(--plum)"/><rect x="35" y="31" width="22" height="18" fill="var(--plum)"/><circle cx="58" cy="48" r="8" fill="#fff" stroke="var(--ink)" stroke-width="3"/></svg>
  <h3>Maintenance<br>&amp; Backup</h3>
  <p>printing and typesetting istry.<br>Ipsum has been the industry's sta.</p>
  <div class="go"><svg width="10" height="10"><use href="#arrow"/></svg></div>
</div>

<!-- testimonials -->
<section class="abs testimonials" role="img" aria-label="Faded grid of portrait photographs behind the testimonials"></section>
<h2 class="abs sec-title" style="top:1501px">Client <b>Testimonials</b></h2>
<svg class="abs sec-bulb" style="top:1555px" width="24" height="30" viewBox="0 0 100 130"><use href="#bulb"/></svg>

<article class="abs card" style="left:99px">
  <p>Lorem ipsum dolor sit amet, consectetuer adipiscing elit, sed diam nonummy nibh euismod tincidunt ut laoreet dolore .</p>
  <div class="person"><div class="avatar" role="img" aria-label="Headshot of the client"></div><div><strong>Marcus Fell</strong><span>Professional Racer</span></div></div>
</article>
<article class="abs card" style="left:441px">
  <p>Lorem ipsum dolor sit amet, consectetuer adipiscing elit, sed diam nonummy nibh euismod tincidunt ut laoreet dolore .</p>
  <div class="person"><div class="avatar" role="img" aria-label="Headshot of the client"></div><div><strong>Marcus Fell</strong><span>Professional Racer</span></div></div>
</article>
<article class="abs card" style="left:784px">
  <p>Lorem ipsum dolor sit amet, consectetuer adipiscing elit, sed diam nonummy nibh euismod tincidunt ut laoreet dolore .</p>
  <div class="person"><div class="avatar" role="img" aria-label="Headshot of the client"></div><div><strong>Marcus Fell</strong><span>Professional Racer</span></div></div>
</article>

<!-- footer -->
<footer class="abs footer"></footer>
<div class="abs col quick" style="left:101px">
  <h4>Quick Link</h4>
  <ul><li>Home</li><li>About Us</li><li>Services</li><li>Contact Us</li></ul>
</div>
<div class="abs col news" style="left:311px;width:230px">
  <h4>Join Our Newsletter</h4>
  <p>Subscribe to our Newsletter to get the latest scoop right to your inbox</p>
  <div class="field">Enter Your Email</div>
  <div class="subscribe">Subscribe</div>
</div>
<div class="abs col contact" style="left:580px;width:220px">
  <h4>Contact Detail</h4>
  <p>14 Marlow Close, Fernhollow<br>Ashdale, ZZ9 4QT</p>
  <p style="margin-top:10px">01632 960481<br>info@brightcrest-demo.co.uk</p>
  <div class="soc"><i></i><i></i><i></i></div>
</div>
<div class="abs map" role="img" aria-label="Street map showing the office location"></div>
<svg class="abs" style="left:946px;top:1960px" width="30" height="42" viewBox="0 0 30 42"><path d="M15 41 C15 41 2 24 2 15 A13 13 0 0 1 28 15 C28 24 15 41 15 41Z" fill="var(--plum)"/><circle cx="15" cy="15" r="5" fill="#fff"/></svg>
<a class="abs map-link" href="#">View quorvo Map</a>
<div class="abs base">Copyright © 2016 brightcrest. All Right Reserved.</div>

</body>
</html>
```